Korvane Sky Works, LLC - Business Card

I currently have a drone business that specializes in aerial photography, thermal image inspections, deer recovery, search and rescue, custom agricultural applications. i will attach my current business card as well as some logos to incorporate for a new up to date business card
Updates

Designs look the same

Sick

Target Market(s)

farmers, hunters

Contact Information for Business Card

name address phone number (as existing card i attached)

Requirements
Must have
• im good with existing business card, but would like an agricultural twist

```html
<!DOCTYPE html>
<html lang="en">
<head>
<meta charset="utf-8">
<title>Korvane Sky Works, LLC – Business Card</title>
<link href="https://fonts.googleapis.com/css2?family=Poppins:wght@400;500;600&display=swap" rel="stylesheet">
<style>
  :root {
    --page-bg: #dfdfdf;
    --card-bg: #ffffff;
    --ink: #111111;
    --accent: #ee1c1c;
    --facet-light: #f6f6f6;
    --facet-mid: #efefef;
  }
  * { box-sizing: border-box; margin: 0; padding: 0; }
  html, body { width: 1200px; height: 1125px; overflow: hidden; }
  body {
    background: var(--page-bg);
    font-family: "Poppins", sans-serif;
    color: var(--ink);
    position: relative;
  }
  .card {
    position: absolute;
    width: 787.5px;
    height: 450px;
    background: var(--card-bg);
    overflow: hidden;
  }
  .card-front { left: 75px; top: 75px; }
  .card-back { left: 337.5px; top: 600px; }
  .facets { position: absolute; inset: 0; width: 100%; height: 100%; }

  .brand {
    position: absolute;
    left: 0; right: 0;
    top: 150px;
    display: flex;
    flex-direction: column;
    align-items: center;
  }
  .brand-dot {
    width: 62px; height: 62px;
    border-radius: 50%;
    border: 6px solid var(--accent);
    margin-bottom: 14px;
  }
  .brand-name {
    font-weight: 600;
    font-size: 52px;
    line-height: 1;
    letter-spacing: 3px;
    color: var(--accent);
    text-transform: uppercase;
  }
  .brand-tagline {
    margin-top: 10px;
    font-weight: 600;
    font-size: 19px;
    letter-spacing: 6px;
    color: var(--ink);
  }

  .person {
    position: absolute;
    right: 45px; top: 44px;
    text-align: right;
  }
  .person-name { font-size: 36px; font-weight: 500; line-height: 1.1; letter-spacing: 0.5px; }
  .person-role { font-size: 18px; color: var(--accent); line-height: 1.2; }

  .services {
    position: absolute;
    left: 45px; top: 146px;
    list-style: none;
  }
  .services li {
    display: flex;
    align-items: center;
    font-size: 19.5px;
    height: 28px;
    margin-bottom: 14px;
  }
  .services svg { width: 14px; height: 14px; margin-right: 10px; }

  .contact {
    position: absolute;
    right: 45px; top: 273px;
    text-align: right;
    list-style: none;
    font-size: 19.5px;
  }
  .contact li { height: 34.7px; line-height: 30px; }
</style>
</head>
<body>

<section class="card card-front">
  <svg class="facets" viewBox="0 0 787.5 450" preserveAspectRatio="none" aria-hidden="true">
    <polygon points="0,0 180,0 400,225 180,450 0,450 150,225" fill="var(--facet-light)"/>
    <polygon points="560,0 787.5,0 787.5,40 580,260 787.5,450 600,450 380,225" fill="var(--facet-mid)" opacity="0.6"/>
    <polygon points="130,450 394,190 640,450" fill="var(--facet-light)"/>
  </svg>
  <div class="brand">
    <div class="brand-dot"></div>
    <div class="brand-name">Korvane</div>
    <div class="brand-tagline">DRONE SERVICES</div>
  </div>
</section>

<section class="card card-back">
  <svg class="facets" viewBox="0 0 787.5 450" preserveAspectRatio="none" aria-hidden="true">
    <polygon points="0,0 190,0 430,230 290,230" fill="var(--facet-light)"/>
    <polygon points="787.5,30 560,260 787.5,450" fill="var(--facet-mid)" opacity="0.6"/>
    <polygon points="130,450 365,205 325,450" fill="var(--facet-light)"/>
    <polygon points="420,240 605,450 420,450" fill="var(--facet-mid)" opacity="0.7"/>
  </svg>

  <div class="person">
    <div class="person-name">DALTON REESE</div>
    <div class="person-role">OWNER</div>
  </div>

  <ul class="services">
    <li><svg viewBox="0 0 14 14"><path d="M1 2 L7 7 L1 12 Z M6 2 L13 7 L6 12 L8 7 Z" fill="var(--accent)"/></svg>Thermal Image Inspections</li>
    <li><svg viewBox="0 0 14 14"><path d="M1 2 L7 7 L1 12 Z M6 2 L13 7 L6 12 L8 7 Z" fill="var(--accent)"/></svg>Deer Recovery</li>
    <li><svg viewBox="0 0 14 14"><path d="M1 2 L7 7 L1 12 Z M6 2 L13 7 L6 12 L8 7 Z" fill="var(--accent)"/></svg>Search &amp; Rescue</li>
    <li><svg viewBox="0 0 14 14"><path d="M1 2 L7 7 L1 12 Z M6 2 L13 7 L6 12 L8 7 Z" fill="var(--accent)"/></svg>Real Estate Photography</li>
  </ul>

  <ul class="contact">
    <li>(555)-210-4836</li>
    <li>korvaneskyworks@mail.com</li>
    <li>www.korvaneskyworks.com</li>
    <li>214 W. Elm St. Harlow, OH 45000</li>
  </ul>
</section>

</body>
</html>
```